Brisk Wire Services - Electrical

We need flyers for electrical services.
Areas of work include new builds, office fitouts, switchboard upgrades, installation of ceiling fans, powerpoint and downlight upgrades, home theatre and AV systems, all exterior and emergency work. Free quotes
We would like to see designs with the colour Red with a young and modern design. Licence No: 83146K must be included and call Leopold on 0418693027.

Colors
ec1f27

```html
<!DOCTYPE html>
<html lang="en">
<head>
<meta charset="utf-8">
<title>Brisk Wire Services – Electrical Flyer</title>
<link rel="stylesheet" href="https://fonts.googleapis.com/css2?family=Montserrat:wght@400;700;800&family=Open+Sans:wght@300;400;700&display=swap">
<style>
  :root {
    --red: #ec1f27;
    --red-deep: #8e0d10;
    --red-dark: #4a0608;
    --black: #0b0b0b;
    --ink: #2b2b2b;
    --grey-text: #5a5a5a;
    --panel: #3a3a3c;
    --panel-dark: #1c1c1e;
    --white: #ffffff;
    --stage: #e6e6e8;
  }
  * { box-sizing: border-box; margin: 0; padding: 0; }
  html, body { width: 1200px; height: 1200px; overflow: hidden; background: var(--stage); }
  .canvas { position: relative; width: 1200px; height: 1200px; }

  .flyer {
    position: absolute; left: 197px; top: 30px;
    width: 806px; height: 1140px;
    background: var(--white); overflow: hidden;
    font-family: "Open Sans", sans-serif; color: var(--ink);
    box-shadow: 0 10px 30px rgba(0,0,0,.18);
  }

  .brand {
    position: absolute; left: 56px; top: 72px;
    display: flex; align-items: center; gap: 12px;
  }
  .brand-mark { width: 18px; height: 18px; border-radius: 50%; background: var(--black); }
  .brand-name { font-weight: 700; font-size: 30px; color: var(--red); letter-spacing: -.3px; }

  .hero-band {
    position: absolute; left: 0; top: 168px; width: 600px; height: 372px;
    background: linear-gradient(120deg, var(--red) 0%, var(--red-deep) 45%, var(--red-dark) 100%);
  }
  .headline {
    position: absolute; left: 52px; top: 262px; color: var(--white);
    font-family: "Montserrat", sans-serif; line-height: 1;
  }
  .headline-lead { display: block; font-weight: 400; font-size: 36px; margin-bottom: 8px; }
  .headline-main { display: block; font-weight: 800; font-size: 56px; letter-spacing: 1px; }
  .headline-sub { display: block; font-weight: 800; font-size: 54px; letter-spacing: 1px; margin: 10px 0 0 22px; }

  .side-panel {
    position: absolute; left: 560px; top: 450px; width: 246px; height: 580px;
    background: linear-gradient(180deg, var(--panel) 0%, var(--panel-dark) 100%);
  }
  .hero-circle { position: absolute; left: 430px; top: 40px; width: 410px; height: 410px; }

  .services-tag {
    position: absolute; left: 72px; top: 558px; height: 46px; padding: 0 32px 0 22px;
    background: var(--black); color: var(--white); border-radius: 0 23px 23px 0;
    font-family: "Montserrat", sans-serif; font-weight: 800; font-size: 25px; line-height: 46px;
    letter-spacing: 1px;
  }

  .service { position: absolute; width: 220px; text-align: center; }
  .service-icon { display: block; width: 52px; height: 52px; margin: 0 auto 6px; }
  .service-label {
    font-family: "Montserrat", sans-serif; font-weight: 700; font-size: 16px;
    color: var(--grey-text); line-height: 1.22; letter-spacing: .5px;
  }

  .quote-tab {
    position: absolute; left: 430px; top: 970px; width: 376px; height: 60px;
    background: linear-gradient(90deg, var(--red), #c5161d);
    border-radius: 42px 0 0 0;
    color: var(--white); font-family: "Montserrat", sans-serif; font-weight: 800;
    font-size: 25px; letter-spacing: 1px; line-height: 60px; padding-left: 52px;
  }
  .footer {
    position: absolute; left: 0; top: 1030px; width: 806px; height: 110px;
    background: var(--black); color: var(--white);
  }
  .call { position: absolute; left: 190px; top: 12px; font-family: "Montserrat", sans-serif; line-height: 1.15; }
  .call-name { display: block; font-weight: 400; font-size: 28px; letter-spacing: 1px; }
  .call-number { display: block; font-weight: 800; font-size: 38px; letter-spacing: 1px; margin-top: 2px; }
  .licence { position: absolute; left: 520px; top: 26px; font-family: "Montserrat", sans-serif; font-size: 15px; }
  .licence-label { color: var(--red); }
  .licence-number { color: var(--white); margin-left: 8px; }
</style>
</head>
<body>
<main class="canvas">
  <article class="flyer">

    <div class="hero-band" role="img" aria-label="Red-toned photo of electrical wiring inside a switchboard"></div>

    <header class="brand">
      <span class="brand-mark"></span>
      <span class="brand-name">Brisk Wire Services</span>
    </header>

    <div class="side-panel" role="img" aria-label="Electrician in blue overalls and orange hard hat standing with arms crossed against a dark workshop backdrop"></div>

    <svg class="hero-circle" viewBox="0 0 500 500">
      <defs>
        <radialGradient id="circuitGlow" cx="70%" cy="30%" r="80%">
          <stop offset="0%" stop-color="#f4a25a"/>
          <stop offset="35%" stop-color="#b5502e"/>
          <stop offset="75%" stop-color="#4a2b26"/>
          <stop offset="100%" stop-color="#231a1a"/>
        </radialGradient>
      </defs>
      <circle cx="250" cy="250" r="240" fill="#ffffff"/>
      <path d="M 22 250 A 228 228 0 0 0 250 478" fill="none" stroke="#0b0b0b" stroke-width="14"/>
      <path d="M 250 478 A 228 228 0 0 0 466 320" fill="none" stroke="#ec1f27" stroke-width="14"/>
      <circle cx="250" cy="250" r="212" fill="url(#circuitGlow)" role="img" aria-label="Close-up photo of a hand using tweezers on a circuit board"/>
    </svg>

    <h1 class="headline">
      <span class="headline-lead">For All Your</span>
      <span class="headline-main">Electrical</span>
      <span class="headline-sub">Needs</span>
    </h1>

    <div class="services-tag">Our Services</div>

    <svg width="0" height="0" style="position:absolute">
      <defs>
        <g id="ring">
          <circle cx="30" cy="30" r="26" fill="#fff" stroke="#d7d7d7" stroke-width="1.5"/>
          <path d="M 30 4 A 26 26 0 0 0 8 44" fill="none" stroke="#ec1f27" stroke-width="5"/>
          <path d="M 52 44 A 26 26 0 0 1 30 56" fill="none" stroke="#0b0b0b" stroke-width="5"/>
        </g>
      </defs>
    </svg>

    <div class="service" style="left:70px; top:622px;">
      <svg class="service-icon" viewBox="0 0 60 60"><use href="#ring"/><path d="M19 40 h22 M22 40 v-10 l8-7 8 7 v10" fill="none" stroke="#222" stroke-width="2"/></svg>
      <p class="service-label">New builds</p>
    </div>
    <div class="service" style="left:90px; top:718px;">
      <svg class="service-icon" viewBox="0 0 60 60"><use href="#ring"/><g fill="none" stroke="#222" stroke-width="2"><rect x="18" y="20" width="24" height="20" rx="3"/><circle cx="25" cy="30" r="2"/><circle cx="35" cy="30" r="2"/></g></svg>
      <p class="service-label">Powerpoint and<br>downlight upgrades</p>
    </div>
    <div class="service" style="left:110px; top:826px;">
      <svg class="service-icon" viewBox="0 0 60 60"><use href="#ring"/><path d="M17 40 h26 M20 40 v-11 l10-8 10 8 v11 M27 40 v-7 h6 v7" fill="none" stroke="#222" stroke-width="2"/></svg>
      <p class="service-label">All exterior and<br>emergency work</p>
    </div>
    <div class="service" style="left:140px; top:932px;">
      <svg class="service-icon" viewBox="0 0 60 60"><use href="#ring"/><g fill="none" stroke="#222" stroke-width="2"><rect x="20" y="18" width="16" height="22"/><rect x="26" y="24" width="16" height="18"/></g></svg>
      <p class="service-label">Office fitouts</p>
    </div>

    <div class="service" style="left:320px; top:560px;">
      <svg class="service-icon" viewBox="0 0 60 60"><use href="#ring"/><g fill="none" stroke="#222" stroke-width="2"><circle cx="30" cy="30" r="3"/><ellipse cx="30" cy="20" rx="4" ry="8"/><ellipse cx="39" cy="35" rx="8" ry="4" transform="rotate(30 39 35)"/><ellipse cx="21" cy="35" rx="8" ry="4" transform="rotate(-30 21 35)"/></g></svg>
      <p class="service-label">Installation of<br>ceiling fans</p>
    </div>
    <div class="service" style="left:330px; top:678px;">
      <svg class="service-icon" viewBox="0 0 60 60"><use href="#ring"/><g fill="none" stroke="#222" stroke-width="2"><rect x="16" y="21" width="28" height="18" rx="2"/><path d="M21 27 h18 M21 33 h18"/></g></svg>
      <p class="service-label">Switchboard<br>upgrades</p>
    </div>
    <div class="service" style="left:335px; top:800px;">
      <svg class="service-icon" viewBox="0 0 60 60"><use href="#ring"/><g fill="none" stroke="#222" stroke-width="2"><rect x="16" y="20" width="10" height="20"/><rect x="34" y="20" width="10" height="20"/><circle cx="21" cy="34" r="3"/><circle cx="39" cy="34" r="3"/></g></svg>
      <p class="service-label">Home theatre<br>and AV systems</p>
    </div>

    <div class="quote-tab">FREE QUOTES</div>

    <footer class="footer">
      <div class="call">
        <span class="call-name">CALL LEOPOLD</span>
        <span class="call-number">04-1869-3027</span>
      </div>
      <p class="licence"><span class="licence-label">Licence No:</span><span class="licence-number">83146K</span></p>
    </footer>

  </article>
</main>
</body>
</html>
```